Bright Oak Fitness Facility Business Cards

Business Card Design that incorporates the logo and tagline

Target Market(s)

Fitness, People Who Exercise

Contact Information for Business Card

2817 Mossgrove Bend Road
Fernmoor, Oregon 97190
Phone: 352-555-Jump (5867)
www.brightoakfitness.example
info@brightoakfitness.example

Requirements
Must have
• Logo, Address, Website, email and tagline "Stronger Every Day". Colors should be red/black/grey/white

```html
<!DOCTYPE html>
<html lang="en">
<head>
<meta charset="utf-8">
<title>Bright Oak Fitness – Business Card</title>
<link rel="stylesheet" href="https://fonts.googleapis.com/css2?family=Montserrat:wght@500;600&family=Open+Sans:wght@400&display=swap">
<style>
  :root {
    --page-bg: #e6e6e6;
    --card-white: #fbfbfb;
    --brand-red: #e3141b;
    --ink-black: #111111;
    --band-black: #050505;
    --text-dark: #1c1c1c;
    --text-light: #ffffff;
  }
  * { box-sizing: border-box; margin: 0; padding: 0; }
  html, body { width: 1200px; height: 900px; overflow: hidden; }
  body { background: var(--page-bg); position: relative; }

  .business-card {
    position: absolute;
    left: 160px; top: 177px;
    width: 880px; height: 546px;
    background: var(--card-white);
    box-shadow: 0 6px 24px rgba(0,0,0,0.15);
    overflow: hidden;
  }
  .brand-block {
    position: absolute;
    left: 0; right: 0; top: 150px;
    display: flex; justify-content: center; align-items: center; gap: 16px;
  }
  .brand-dot {
    width: 22px; height: 22px; border-radius: 50%;
    background: var(--brand-red);
  }
  .brand-name {
    font-family: "Montserrat", sans-serif;
    font-weight: 600;
    font-size: 44px;
    letter-spacing: 0.5px;
    text-transform: uppercase;
    color: var(--ink-black);
  }
  .tagline {
    position: absolute;
    left: 0; right: 0; top: 282px;
    text-align: center;
    font-family: "Montserrat", sans-serif;
    font-weight: 500;
    font-size: 23px;
    color: var(--text-dark);
  }
  .contact-band {
    position: absolute;
    left: 0; right: 0; bottom: 0;
    height: 184px;
    background: var(--band-black);
    border-top: 5px solid var(--brand-red);
  }
  .band-marker {
    position: absolute;
    left: 50%; top: -15px;
    width: 24px; height: 24px;
    margin-left: -12px;
    border-radius: 50%;
    background: var(--brand-red);
  }
  .contact-list {
    position: absolute;
    left: 39px; top: 48px;
    list-style: none;
    font-family: "Open Sans", sans-serif;
    font-size: 23px;
    color: var(--text-light);
    line-height: 31px;
  }
  .contact-list li { display: flex; align-items: center; gap: 8px; }
  .contact-icon { width: 18px; height: 18px; fill: var(--text-light); flex: none; }
  .address {
    position: absolute;
    right: 42px; top: 48px;
    font-family: "Open Sans", sans-serif;
    font-style: normal;
    font-size: 23px;
    line-height: 31px;
    color: var(--text-light);
    text-align: right;
  }
</style>
</head>
<body>
  <section class="business-card">
    <div class="brand-block">
      <span class="brand-dot"></span>
      <span class="brand-name">Bright Oak Fitness</span>
    </div>
    <p class="tagline">STRONGER EVERY DAY</p>

    <div class="contact-band">
      <span class="band-marker"></span>
      <ul class="contact-list">
        <li>
          <svg class="contact-icon" viewBox="0 0 24 24" aria-hidden="true"><path d="M6.6 10.8a15.1 15.1 0 0 0 6.6 6.6l2.2-2.2c.3-.3.7-.4 1-.2 1.1.4 2.3.6 3.6.6.6 0 1 .4 1 1V20c0 .6-.4 1-1 1A17 17 0 0 1 3 4c0-.6.4-1 1-1h3.5c.6 0 1 .4 1 1 0 1.3.2 2.5.6 3.6.1.3 0 .7-.2 1z"/></svg>
          352-555-Jump (5867)
        </li>
        <li>
          <svg class="contact-icon" viewBox="0 0 24 24" aria-hidden="true"><path d="M2 5h20v14H2V5zm2 2v.4l8 5.6 8-5.6V7H4z"/></svg>
          info@brightoakfitness.example
        </li>
        <li>
          <svg class="contact-icon" viewBox="0 0 24 24" aria-hidden="true"><path d="M12 2a10 10 0 1 0 0 20 10 10 0 0 0 0-20zm-1 17.9A8 8 0 0 1 4.2 10.2L9 15v1a2 2 0 0 0 2 2v1.9zm6.9-2.5A2 2 0 0 0 16 16h-1v-3a1 1 0 0 0-1-1H8v-2h2a1 1 0 0 0 1-1V7h2a2 2 0 0 0 2-2v-.4a8 8 0 0 1 2.9 12.8z"/></svg>
          www.brightoakfitness.example
        </li>
      </ul>
      <address class="address">
        2817 Mossgrove Bend Road<br>
        Fernmoor, Oregon 97190
      </address>
    </div>
  </section>
</body>
</html>
```